Web Design Project for a new download application :-)

We need a website design and a logo design for a new website and desktop application.
The Website will be www.Fetchora.com
The installed application will be: Fetchora

Fetchora is a desktop application that searches and finds all kind of Media files (Movies, Games, Songs, software, etc..)
Fetchora will also manage the download process for the selected files.
Fetchora automates the whole search and download process.

User Flow:
users will initially visit the website.
user will download the application from the website
user will install the application on his computer.
user will run and use the application.

What makes our software special:
-Great search engine for searching media files.
-Very high speed downloads. maximum speeds.
-Allow used to Search by: file type, size, date, format
-Pause and resume downloads
-Get any file you want instantly.
-Unlimited Downloads.

We will need:
Logo
WebSite Design
Icons for the desktop application.

we need only PSDs - no codded pages are needed !

Design to the following screen Size & resolution: 1024 x 768

Target Market(s)

movies and music lovers.
users who download movies, games, softwares, music etc...

Industry/Entity Type

Software

Requirements
Must have
• must have download button

Files

```html
<!DOCTYPE html>
<html lang="en">
<head>
<meta charset="utf-8">
<title>Fetchora – media search engine</title>
<link rel="stylesheet" href="https://fonts.googleapis.com/css2?family=Source+Sans+3:wght@400;600;700&display=swap">
<style>
  :root {
    --green: #5cb531;
    --green-dark: #3f9a1d;
    --green-light: #8fd34f;
    --ink: #6a6a6a;
    --ink-dark: #4a4a4a;
    --ink-soft: #8a8a8a;
    --line: #cfcfcf;
    --arrow: #8c8c8c;
    --tile-edge: #b9b9b9;
    --social: #9a9a9a;
    --bg: #ffffff;
  }
  * { box-sizing: border-box; margin: 0; padding: 0; }
  html, body { width: 1200px; height: 600px; overflow: hidden; background: var(--bg); }
  body { font-family: "Source Sans 3", "Myriad Pro", Arial, sans-serif; color: var(--ink); position: relative; }

  .site-header {
    position: absolute; left: 0; top: 0; width: 1200px; height: 110px;
    background: linear-gradient(#ffffff 0%, #f0f0f0 45%, #e2e2e2 62%, #f4f4f4 80%, #ffffff 100%);
  }
  .brand { position: absolute; left: 44px; top: 14px; }
  .brand-name { font-size: 58px; font-weight: 700; color: var(--ink); line-height: 1; letter-spacing: -1px; }
  .brand-tagline { font-size: 21px; color: var(--ink-soft); margin-left: 46px; line-height: 1; }

  .search-field {
    position: absolute; left: 587px; top: 13px; width: 195px; height: 21px;
    border: 1px solid #cfcfcf; background: #f6f6f6; font-size: 12px; color: var(--ink);
    padding: 2px 6px;
  }
  .account-links { position: absolute; left: 788px; top: 15px; font-size: 13px; color: var(--ink); }
  .account-links span { color: #bdbdbd; }
  .btn-app {
    position: absolute; left: 917px; top: 13px; width: 134px; height: 21px;
    background: linear-gradient(var(--green-light), var(--green)); color: #fff;
    font-size: 13px; text-align: center; line-height: 19px; border: 1px solid var(--green-dark);
  }
  .languages { position: absolute; left: 1104px; top: 18px; display: flex; gap: 3px; }
  .languages i { display: block; width: 18px; height: 11px; }

  .main-nav { position: absolute; left: 546px; top: 66px; display: flex; }
  .main-nav a {
    display: block; height: 26px; width: 117px; margin-right: 4px; text-decoration: none;
    background: linear-gradient(var(--green-light), var(--green)); color: #fff; font-size: 15px;
    text-align: center; line-height: 26px; border-radius: 3px 3px 0 0;
  }
  .main-nav .home { width: 30px; margin-right: 12px; background: none; }

  .intro { position: absolute; left: 24px; top: 133px; width: 340px; }
  .intro h1 { font-size: 37px; font-weight: 700; color: var(--ink); line-height: 44px; margin-bottom: 2px; letter-spacing: -0.3px; }
  .intro p { font-size: 14px; line-height: 17px; margin-bottom: 17px; color: var(--ink); }
  .intro b { color: var(--ink-dark); }
  .btn-download {
    position: absolute; left: 24px; top: 430px; width: 249px; height: 36px;
    background: linear-gradient(var(--green-light), var(--green)); color: #fff; font-size: 21px;
    text-align: center; line-height: 36px; border-radius: 2px;
  }

  .diagram { position: absolute; left: 0; top: 0; }
  .tile-label { font-size: 11px; fill: var(--ink); text-anchor: middle; font-family: "Source Sans 3", Arial, sans-serif; }

  .site-footer { position: absolute; left: 0; top: 490px; width: 1200px; height: 110px; }
  .footer-col { position: absolute; top: 10px; font-size: 11px; line-height: 13.6px; color: var(--ink); }
  .footer-col h3 { font-size: 11px; font-weight: 700; color: var(--green-dark); margin-bottom: 6px; }
  .footer-divider { position: absolute; top: 10px; width: 1px; height: 90px; background: var(--line); }
  .storage-count { font-size: 30px; line-height: 30px; color: var(--ink); margin-top: 20px; }
  .social { display: flex; gap: 6px; margin-top: 18px; }
  .social span { display: flex; flex-direction: column; align-items: center; gap: 2px; font-size: 8px; line-height: 9px; width: 40px; }
  .social i { display: block; width: 26px; height: 26px; background: var(--social); }
  .copyright { position: absolute; left: 636px; top: 46px; font-size: 10px; color: var(--ink); display: flex; align-items: baseline; gap: 6px; white-space: nowrap; }
  .copyright .footer-brand { font-size: 19px; font-weight: 700; color: var(--ink); }
  .copyright a { color: var(--green-dark); text-decoration: none; }
</style>
</head>
<body>

<header class="site-header">
  <div class="brand">
    <div class="brand-name">Fetchora</div>
    <div class="brand-tagline">media search engine</div>
  </div>
  <div class="search-field">Search media . . .</div>
  <div class="account-links">Sign in <span>| Register | Help</span></div>
  <div class="btn-app">get Fetchora App</div>
  <div class="languages">
    <i role="img" aria-label="English flag" style="background:#2b3f8f"></i>
    <i role="img" aria-label="French flag" style="background:linear-gradient(90deg,#2b3f8f 33%,#fff 33% 66%,#d22 66%)"></i>
    <i role="img" aria-label="German flag" style="background:linear-gradient(#111 33%,#d00 33% 66%,#fc0 66%)"></i>
    <i role="img" aria-label="Spanish flag" style="background:linear-gradient(#c60b1e 25%,#ffc400 25% 75%,#c60b1e 75%)"></i>
  </div>
  <nav class="main-nav">
    <a class="home" href="#" aria-label="Home">
      <svg width="28" height="26" viewBox="0 0 28 26"><path d="M14 2 L27 14 H23 V25 H17 V18 H11 V25 H5 V14 H1 Z" fill="var(--green)"/></svg>
    </a>
    <a href="#">Categories</a>
    <a href="#">Browse media</a>
    <a href="#">New media</a>
    <a href="#">News</a>
    <a href="#">About us</a>
  </nav>
</header>

<section class="intro">
  <h1>Welcome to Fetchora</h1>
  <p><b>Fetchora</b> is the largest media search engine libery<br>where you can search and download<br>any of your favorite media contents.</p>
  <p><b>FAST</b>, <b>RELIABLE</b> and <b>SECURE . . .</b><br><b>Fetchora</b> will make your search and download<br>an interesting and entertaining<br>and most importantly free.</p>
  <p>So hurry up and download <b>Fetchora</b> witch gives you<br>the freedom to choose directly to your computer<br>mobile phones and other multi tasks devices.<br><b>FREEDOM IS YOUR CHOICE !</b></p>
</section>
<div class="btn-download">get Fetchora Now !</div>

<svg class="diagram" width="1200" height="490" viewBox="0 0 1200 490">
  <defs>
    <linearGradient id="tileFill" x1="0" y1="0" x2="0" y2="1">
      <stop offset="0" stop-color="#f2f2f2"/><stop offset="1" stop-color="#d6d6d6"/>
    </linearGradient>
    <linearGradient id="appIconFill" x1="0" y1="0" x2="0" y2="1">
      <stop offset="0" stop-color="#f4f4f4"/><stop offset="0.55" stop-color="#e6e6e6"/><stop offset="1" stop-color="#d2d2d2"/>
    </linearGradient>
    <radialGradient id="globeFill" cx="0.4" cy="0.4" r="0.7">
      <stop offset="0" stop-color="#4a9be6"/><stop offset="1" stop-color="#0d4fa8"/>
    </radialGradient>
  </defs>

  <circle cx="490" cy="297" r="70" fill="url(#globeFill)" role="img" aria-label="Globe with magnifying glass"/>

  <g fill="var(--arrow)">
    <rect x="595" y="183" width="7" height="227"/>
    <rect x="570" y="294" width="28" height="7"/>
    <polygon points="556,297 574,286 574,308"/>
    <rect x="598" y="182" width="28" height="7"/><polygon points="638,185 622,174 622,196"/>
    <rect x="598" y="294" width="28" height="7"/><polygon points="638,297 622,286 622,308"/>
    <rect x="598" y="405" width="28" height="7"/><polygon points="638,408 622,397 622,419"/>
  </g>
  <g fill="var(--arrow)">
    <rect x="968" y="183" width="7" height="227"/>
    <rect x="946" y="182" width="24" height="7"/><polygon points="934,185 950,174 950,196"/>
    <rect x="946" y="294" width="24" height="7"/><polygon points="934,297 950,286 950,308"/>
    <rect x="946" y="405" width="24" height="7"/><polygon points="934,408 950,397 950,419"/>
    <rect x="972" y="294" width="32" height="7"/><polygon points="1018,297 1002,286 1002,308"/>
  </g>

  <g stroke="var(--tile-edge)" stroke-width="1" fill="url(#tileFill)">
    <rect x="648" y="144" width="80" height="80" rx="6"/>
    <rect x="746" y="144" width="80" height="80" rx="6"/>
    <rect x="845" y="144" width="80" height="80" rx="6"/>
    <rect x="648" y="252" width="80" height="80" rx="6"/>
    <rect x="746" y="252" width="80" height="80" rx="6"/>
    <rect x="845" y="252" width="80" height="80" rx="6"/>
    <rect x="648" y="360" width="80" height="80" rx="6"/>
    <rect x="746" y="360" width="80" height="80" rx="6"/>
    <rect x="845" y="360" width="80" height="80" rx="6"/>
  </g>
  <g>
    <rect x="666" y="162" width="44" height="44" rx="8" fill="#555" role="img" aria-label="Music speaker icon"/>
    <rect x="764" y="162" width="44" height="44" rx="4" fill="#333" role="img" aria-label="Film strip icon"/>
    <rect x="863" y="162" width="44" height="44" rx="4" fill="#4ba6dc" role="img" aria-label="Photo icon"/>
    <rect x="666" y="270" width="44" height="44" rx="8" fill="#1d7fd0" role="img" aria-label="Music note icon"/>
    <rect x="764" y="270" width="44" height="44" rx="8" fill="#e0a040" role="img" aria-label="Paint palette icon"/>
    <rect x="863" y="270" width="44" height="44" rx="4" fill="#c2651c" role="img" aria-label="Television icon"/>
    <rect x="666" y="378" width="44" height="44" rx="8" fill="#8c4fa8" role="img" aria-label="Puzzle piece icon"/>
    <rect x="764" y="378" width="44" height="44" rx="4" fill="#2a2a2a" role="img" aria-label="Terminal window icon"/>
    <rect x="863" y="378" width="44" height="44" rx="4" fill="#e6c35a" role="img" aria-label="Folder icon"/>
  </g>
  <text class="tile-label" x="688" y="240">music</text>
  <text class="tile-label" x="786" y="240">videos</text>
  <text class="tile-label" x="885" y="240">photos</text>
  <text class="tile-label" x="688" y="348">sounds</text>
  <text class="tile-label" x="786" y="348">wallpapers</text>
  <text class="tile-label" x="885" y="348">tw shovs</text>
  <text class="tile-label" x="688" y="456">applications</text>
  <text class="tile-label" x="786" y="457">softwares</text>
  <text class="tile-label" x="885" y="456">tipe of files</text>

  <rect x="1030" y="230" width="138" height="146" rx="14" fill="url(#appIconFill)" stroke="#bdbdbd" stroke-width="3" role="img" aria-label="Fetchora application icon"/>
</svg>

<footer class="site-footer">
  <div class="footer-col" style="left:15px">
    <h3>Looking for a . . .</h3>
    Music<br>Movies<br>Wallpapers<br>Games<br>Softwares . . .
  </div>
  <div class="footer-divider" style="left:160px"></div>
  <div class="footer-col" style="left:175px">
    <h3>About . . .</h3>
    About us<br>How it Works<br>Contact us<br>Help<br>Blog
  </div>
  <div class="footer-divider" style="left:268px"></div>
  <div class="footer-col" style="left:300px">
    <h3>Recent media storage . . .</h3>
    <div class="storage-count">298,653</div>
  </div>
  <div class="footer-divider" style="left:468px"></div>
  <div class="footer-col" style="left:501px">
    <h3>Follow us . . .</h3>
    <div class="social">
      <span><i></i>Friendloop</span>
      <span><i></i>Chirpline</span>
      <span><i></i>RSS</span>
    </div>
  </div>
  <div class="copyright">
    <span class="footer-brand">Fetchora</span>
    <span>Copyright © 2011 Fetchora. Use of this website constitutes acceptance of our <a href="#">User Agreement</a> and <a href="#">Privacy Policy.</a></span>
  </div>
</footer>

</body>
</html>
```